Real Estate Investment Company Needs A Business Card Designed

I need a business card designed for my use. We are a real estate investment company based in Omaha, Nebraska that specializes in buying, rehabbing and selling single family and multifamily properties. Would love designs that incorporate our logo and colors

Industry/Entity Type

Business

Contact Information for Business Card

Marlow Pettigrew | President & CEO
4837 North 52nd Avenue, Ste 200
Omaha, NE 68214
(402) 555-7428
marlow@quillfenhomes.example
www.QuillfenHomes.example

Font styles to use
Serif

Colors
0255a3
3276b5

Requirements
Must have
• Our logo

```html
<!DOCTYPE html>
<html lang="en">
<head>
<meta charset="utf-8">
<title>Quillfen Homes – Business Card</title>
<link href="https://fonts.googleapis.com/css2?family=Lato:wght@400;700&display=swap" rel="stylesheet">
<style>
  :root{
    --backdrop:#9a9a9a;
    --card-dark:#2f2f2f;
    --brand-blue:#3f97e6;
    --brand-blue-light:#55a8f0;
    --brand-blue-deep:#2a78c6;
    --silver-light:#e2e2e2;
    --silver-dark:#a9a9a9;
    --text-light:#e6e6e6;
    --white:#ffffff;
  }
  html,body{margin:0;padding:0;width:1200px;height:900px;overflow:hidden;background:var(--backdrop);font-family:'Lato',sans-serif;}
  .canvas{position:relative;width:1200px;height:900px;}
  .card{position:absolute;top:306px;width:440px;height:272px;overflow:hidden;}
  .card-front{left:149px;background:var(--card-dark);}
  .card-back{left:608px;background:linear-gradient(180deg,var(--silver-light),var(--silver-dark));}

  .name-accent{position:absolute;left:0;top:26px;}
  .holder{position:absolute;left:41px;top:33px;}
  .holder-name{margin:0;font-size:16.5px;font-weight:700;letter-spacing:.2px;color:var(--brand-blue);line-height:1;}
  .holder-name .first{color:var(--brand-blue-light);}
  .holder-title{margin:2px 0 0;font-size:12.5px;line-height:14px;color:var(--text-light);}

  .address{position:absolute;left:16px;top:146px;font-size:13px;line-height:16px;color:var(--text-light);margin:0;font-style:normal;}
  .contacts{position:absolute;left:16px;top:194px;list-style:none;margin:0;padding:0;font-size:13px;line-height:16px;color:var(--text-light);}
  .contacts li{display:flex;align-items:center;gap:4px;}
  .contacts svg{width:10px;height:10px;fill:var(--brand-blue);}

  .brand{position:absolute;left:280px;top:62px;width:150px;text-align:center;}
  .brand-circle{display:block;margin:0 auto 12px;}
  .brand-name{margin:0;font-size:19px;font-weight:700;letter-spacing:.5px;line-height:22px;color:var(--brand-blue);}

  .bottom-band{position:absolute;left:0;bottom:0;}

  .back-blue{position:absolute;left:0;top:0;width:224px;height:272px;background:linear-gradient(180deg,var(--brand-blue-light),var(--brand-blue-deep));}
  .back-circle{position:absolute;left:106px;top:46px;width:220px;height:220px;border:6px solid var(--white);border-radius:50%;box-sizing:border-box;}
  .back-name{position:absolute;left:106px;top:46px;width:220px;height:220px;margin:0;display:flex;flex-direction:column;align-items:center;justify-content:center;font-size:28px;font-weight:700;letter-spacing:1px;color:var(--white);line-height:34px;text-align:center;}
</style>
</head>
<body>
<main class="canvas">
  <section class="card card-front" aria-label="Business card front">
    <svg class="name-accent" width="30" height="38" viewBox="0 0 30 38" aria-hidden="true">
      <polygon points="0,0 18,0 18,38 6,38" fill="#d8d8d8"/>
      <polygon points="12,0 28,0 28,38 20,38" fill="var(--brand-blue)"/>
    </svg>
    <div class="holder">
      <h1 class="holder-name"><span class="first">MARLOW</span> PETTIGREW</h1>
      <p class="holder-title">President &amp; CEO</p>
    </div>

    <address class="address">4837 North 52nd Avenue, Ste 200<br>Omaha, NE 68214</address>
    <ul class="contacts">
      <li><svg viewBox="0 0 10 10" aria-hidden="true"><path d="M1 3c0-1 1-2 4-2s4 1 4 2v1H7V3H3v1H1z M2 5h6l1 4H1z"/></svg>(402) 555-7428</li>
      <li><svg viewBox="0 0 10 10" aria-hidden="true"><path d="M0 2h10v6H0z" /><path d="M0 2l5 3 5-3" stroke="#2f2f2f" stroke-width="1" fill="none"/></svg>marlow@quillfenhomes.example</li>
      <li><svg viewBox="0 0 10 10" aria-hidden="true"><circle cx="5" cy="5" r="4.5"/></svg>www.QuillfenHomes.example</li>
    </ul>

    <div class="brand">
      <svg class="brand-circle" width="90" height="90" viewBox="0 0 90 90" aria-hidden="true">
        <circle cx="45" cy="45" r="41" fill="none" stroke="var(--brand-blue)" stroke-width="4"/>
      </svg>
      <p class="brand-name">QUILLFEN<br>HOMES</p>
    </div>

    <svg class="bottom-band" width="440" height="16" viewBox="0 0 440 16" aria-hidden="true">
      <defs>
        <linearGradient id="band-silver" x1="0" y1="0" x2="0" y2="1"><stop offset="0" stop-color="#f0f0f0"/><stop offset="1" stop-color="#b8b8b8"/></linearGradient>
      </defs>
      <polygon points="0,1 234,1 224,16 0,16" fill="url(#band-silver)"/>
      <polygon points="236,1 440,1 440,16 222,16" fill="var(--brand-blue)"/>
    </svg>
  </section>

  <section class="card card-back" aria-label="Business card back">
    <div class="back-blue"></div>
    <div class="back-circle" aria-hidden="true"></div>
    <p class="back-name"><span>QUILLFEN</span><span>HOMES</span></p>
  </section>
</main>
</body>
</html>
```